smart logo for a small painting company located in rainy Vancouver Bc *

I need a logo design for business cards and vehicle signage that will cover the entire work van.
Colors: I am open minded
Its a residential/commercial painting company.
I live in the rain forest of western canada. Raincity Vancouver Bc.
I want something that makes people think of the environment as Precious.
I would like to see designs from conservative to wild and crazy.

Target Market(s)

high end residential/commercial painting

Industry/Entity Type

Painting And Decorating

Contact Information for Business Card

On the Front, Just the logo with the logo text. the card stock should have no white showing.
On the Back: Copper Finch Coatings Company
Owner:Darel Hunsaker
Phone:604 318 2465
Email:copperfinchcoatings@mailvista.net
Fully insured, Clean, Quality Service.

Logo Text

Copper Finch Coatings Company

Font styles to use
Other font styles liked:
• Axis

Colors

Designer to choose colors to be used in the design.

Requirements
Must have
• My project must have bold colors.
Nice to have
• A tree frog walking through paint and tracking it up the side of a building
• A tree frog being painted by an artist.
• A paisley tree frog.
Should not have
• A beret. This frog isn't french.

```html
<!DOCTYPE html>
<html lang="en">
<head>
<meta charset="utf-8">
<title>Copper Finch Coatings Company – Business Card</title>
<link rel="stylesheet" href="https://fonts.googleapis.com/css2?family=Quicksand:wght@700&display=swap">
<style>
  :root {
    --page-bg: #ebebeb;
    --forest: #073300;
    --forest-soft: #1d5a0a;
    --signal-red: #e8231e;
    --lime-light: #d9f53c;
    --lime-mid: #a6e61f;
    --lime-deep: #6fcf14;
    --band-green: #00dc3a;
    --sky-deep: #1760ec;
    --sky-light: #00c8ff;
    --icon-blue: #1d55f0;
    --frog-pale: #d4e6b0;
    --frog-belly: #f3ddd2;
  }
  * { box-sizing: border-box; margin: 0; padding: 0; }
  html, body {
    width: 1189px; height: 1200px; overflow: hidden;
    background: var(--page-bg);
    font-family: "Quicksand", "Arial Rounded MT Bold", sans-serif;
    font-weight: 700;
  }
  .card {
    position: absolute; left: 120px; width: 967px; height: 582px; overflow: hidden;
  }
  .card--front { top: 12px; }
  .card--back { top: 607px; height: 583px; }
  .card__art { position: absolute; inset: 0; width: 100%; height: 100%; }
  .brand { position: absolute; color: var(--forest); line-height: 1; }
  .brand__main { display: block; font-size: 64px; letter-spacing: 2px; }
  .brand__sub { display: block; font-size: 32px; letter-spacing: 1px; margin-top: 14px; }
  .card--front .brand { left: 86px; top: 300px; }
  .card--back .brand { left: 250px; top: 78px; }
  .frog-art { position: absolute; left: 172px; top: 85px; width: 186px; height: 190px; }
  .contact { position: absolute; right: 105px; top: 308px; text-align: right; color: var(--signal-red); }
  .contact__tagline { font-size: 23px; letter-spacing: 1px; }
  .contact__row {
    display: flex; align-items: center; justify-content: flex-end; gap: 26px;
    font-size: 22px; margin-top: 18px;
  }
  .contact__row + .contact__row { margin-top: 14px; }
  .contact__icon { width: 38px; height: 38px; flex: none; }
  .owner { position: absolute; left: 100px; top: 476px; text-align center; text-align: center; }
  .owner__name { font-size: 32px; color: var(--forest); letter-spacing: 1px; }
  .owner__role { font-size: 18px; color: var(--signal-red); letter-spacing: 9px; margin-top: 4px; }
</style>
</head>
<body>

<section class="card card--front">
  <svg class="card__art" viewBox="0 0 1192 717" preserveAspectRatio="none">
    <defs>
      <radialGradient id="front-field" cx="0.45" cy="0.1" r="0.95">
        <stop offset="0" stop-color="var(--lime-light)"/>
        <stop offset="0.55" stop-color="var(--lime-mid)"/>
        <stop offset="1" stop-color="var(--lime-deep)"/>
      </radialGradient>
      <linearGradient id="front-water" x1="0" x2="1" y1="0" y2="0">
        <stop offset="0" stop-color="var(--sky-deep)"/>
        <stop offset="1" stop-color="var(--sky-light)"/>
      </linearGradient>
      <linearGradient id="front-tree-tone" x1="0" x2="0" y1="0" y2="1">
        <stop offset="0" stop-color="var(--forest)"/>
        <stop offset="1" stop-color="var(--forest-soft)"/>
      </linearGradient>
    </defs>
    <rect width="1192" height="717" fill="url(#front-field)"/>
    <rect role="img" aria-label="Dark green tree silhouette illustration" x="905" y="0" width="287" height="560" rx="40" fill="url(#front-tree-tone)"/>
    <path fill="var(--forest)" d="M0,717 C400,600 800,470 1030,505 C1110,515 1160,545 1192,572 L1192,717 Z"/>
    <path fill="var(--band-green)" d="M0,717 C420,625 820,530 1040,532 C1120,535 1170,560 1192,588 L1192,717 Z"/>
    <path fill="url(#front-water)" d="M20,717 C450,660 850,565 1060,568 C1130,572 1170,600 1192,628 L1192,717 Z"/>
    <rect x="14" y="33" width="1163" height="664" rx="60" fill="none" stroke="var(--signal-red)" stroke-width="2" stroke-dasharray="3 5"/>
  </svg>
  <svg class="frog-art" viewBox="0 0 186 190" role="img" aria-label="Watercolour illustration of a tree frog sitting">
    <defs>
      <radialGradient id="frog-tone" cx="0.5" cy="0.6" r="0.6">
        <stop offset="0" stop-color="var(--frog-belly)"/>
        <stop offset="1" stop-color="var(--frog-pale)"/>
      </radialGradient>
    </defs>
    <ellipse cx="93" cy="100" rx="88" ry="88" fill="url(#frog-tone)"/>
  </svg>
  <div class="brand">
    <span class="brand__main">Copper Finch</span>
    <span class="brand__sub">Coatings Company</span>
  </div>
</section>

<section class="card card--back">
  <svg class="card__art" viewBox="0 0 1192 719" preserveAspectRatio="none">
    <defs>
      <radialGradient id="back-field" cx="0.55" cy="0.05" r="0.95">
        <stop offset="0" stop-color="var(--lime-light)"/>
        <stop offset="0.55" stop-color="var(--lime-mid)"/>
        <stop offset="1" stop-color="var(--lime-deep)"/>
      </radialGradient>
      <linearGradient id="back-water" x1="0" x2="1" y1="0" y2="0">
        <stop offset="0" stop-color="var(--sky-deep)"/>
        <stop offset="1" stop-color="var(--sky-light)"/>
      </linearGradient>
      <linearGradient id="back-tree-tone" x1="0" x2="0" y1="0" y2="1">
        <stop offset="0" stop-color="var(--forest)"/>
        <stop offset="1" stop-color="var(--forest-soft)"/>
      </linearGradient>
    </defs>
    <rect width="1192" height="719" fill="url(#back-field)"/>
    <rect role="img" aria-label="Dark green tree silhouette illustration" x="0" y="0" width="282" height="570" rx="40" fill="url(#back-tree-tone)"/>
    <path fill="var(--forest)" d="M0,585 C120,505 260,495 400,525 C700,590 1000,700 1192,719 L0,719 Z"/>
    <path fill="var(--band-green)" d="M0,610 C120,540 260,535 400,560 C700,620 1000,705 1192,719 L0,719 Z"/>
    <path fill="url(#back-water)" d="M0,640 C120,575 260,565 420,590 C720,640 1000,710 1192,719 L0,719 Z"/>
    <rect x="14" y="27" width="1160" height="665" rx="60" fill="none" stroke="var(--signal-red)" stroke-width="2" stroke-dasharray="3 5"/>
  </svg>
  <div class="brand">
    <span class="brand__main">Copper Finch</span>
    <span class="brand__sub">Coatings Company</span>
  </div>
  <div class="contact">
    <p class="contact__tagline">Fully insured, Clean, Quality Service.</p>
    <p class="contact__row">
      <span>copperfinchcoatings@mailvista.net</span>
      <svg class="contact__icon" viewBox="0 0 38 38" aria-hidden="true">
        <circle cx="19" cy="19" r="19" fill="var(--icon-blue)"/>
        <rect x="10" y="12.5" width="18" height="13" rx="1.5" fill="none" stroke="#fff" stroke-width="2"/>
        <path d="M10.5,13.5 L19,20.5 L27.5,13.5" fill="none" stroke="#fff" stroke-width="2"/>
      </svg>
    </p>
    <p class="contact__row">
      <span>604 318 2465</span>
      <svg class="contact__icon" viewBox="0 0 38 38" aria-hidden="true">
        <circle cx="19" cy="19" r="19" fill="var(--icon-blue)"/>
        <path fill="#fff" d="M13,10 L16.5,10 L18,15 L15.8,16.8 C17,19.5 18.7,21.3 21.3,22.4 L23.1,20.2 L28,21.7 L28,25.2 C28,26.5 27,27.4 25.7,27.3 C17.6,26.6 11.4,20.4 10.7,12.3 C10.6,11 11.6,10 13,10 Z"/>
      </svg>
    </p>
  </div>
  <div class="owner">
    <p class="owner__name">Darel Hunsaker</p>
    <p class="owner__role">Owner</p>
  </div>
</section>

</body>
</html>
```